New Zealand Marlborough Sauvignon Blanc wine packaging design

We need packaging design for our new wine brand, Dunmore Hale. The wine is a New Zealand Marlborough Sauvignon Blanc. We would like the packaging will portray elegance and style with an understated label. We are looking for a label that portrays the elegance of the French Riviera. The label should be round or pill shaped.
Updates

Industry/Entity Type

Wine

Font styles to use
Serif
Sans Serif

Requirements
Must have
• The words in order of importance: Dunmore Hale, Sauvignon Blanc, Marlborough, New Zealand. It should be fit to the bottle posted in the links
Nice to have
• a pill shape or circular shape
Should not have
• Illustrations of wine bottles, wine glasses, or grapes

```html
<!DOCTYPE html>
<html lang="en">
<head>
<meta charset="utf-8">
<title>Dunmore Hale Sauvignon Blanc – Front Label</title>
<link rel="stylesheet" href="https://fonts.googleapis.com/css2?family=Alike&family=Abril+Fatface&family=Roboto:wght@400&display=swap">
<style>
  :root {
    --page: #ffffff;
    --label-dark: #2c2a26;
    --rule-grey: #c9c9c9;
    --amber: #f4a526;
    --amber-deep: #d9811a;
    --text-light: #f4f4f2;
    --marker: #1a1a1a;
  }
  html, body {
    margin: 0;
    padding: 0;
    width: 1200px;
    height: 3000px;
    overflow: hidden;
    background: var(--page);
  }
  .canvas {
    position: relative;
    width: 1200px;
    height: 3000px;
  }
  .dimension-guides {
    position: absolute;
    left: 0;
    top: 0;
  }
  .dimension-text {
    font-family: "Roboto", Arial, sans-serif;
    font-size: 22px;
    fill: var(--marker);
  }
  .front-label {
    position: absolute;
    left: 365px;
    top: 260px;
    width: 496px;
    height: 624px;
  }
  .arc-varietal {
    font-family: "Alike", Georgia, serif;
    font-size: 50px;
    letter-spacing: 4px;
    fill: var(--amber);
  }
  .arc-region {
    font-family: "Alike", Georgia, serif;
    font-size: 48px;
    letter-spacing: 5px;
    fill: var(--rule-grey);
  }
  .brand-name {
    font-family: "Abril Fatface", Georgia, serif;
    fill: var(--text-light);
  }
  .country {
    font-family: "Alike", Georgia, serif;
    font-size: 15px;
    letter-spacing: 1.5px;
    fill: var(--text-light);
  }
</style>
</head>
<body>
<main class="canvas">

  <svg class="dimension-guides" width="1200" height="1000" viewBox="0 0 1200 1000" aria-label="Label dimensions">
    <defs>
      <marker id="arrow-head" viewBox="0 0 10 10" refX="9" refY="5" markerWidth="8" markerHeight="8" orient="auto-start-reverse">
        <path d="M0 1 L10 5 L0 9" fill="none" stroke="#1a1a1a" stroke-width="1.5"/>
      </marker>
    </defs>
    <line x1="362" y1="192" x2="362" y2="282" stroke="#1a1a1a" stroke-width="1.5"/>
    <line x1="862" y1="192" x2="862" y2="282" stroke="#1a1a1a" stroke-width="1.5"/>
    <line x1="364" y1="204" x2="860" y2="204" stroke="#1a1a1a" stroke-width="1.5" marker-start="url(#arrow-head)" marker-end="url(#arrow-head)"/>
    <text class="dimension-text" x="602" y="188" text-anchor="middle">80mm</text>

    <line x1="286" y1="258" x2="382" y2="258" stroke="#1a1a1a" stroke-width="1.5"/>
    <line x1="286" y1="884" x2="382" y2="884" stroke="#1a1a1a" stroke-width="1.5"/>
    <line x1="295" y1="260" x2="295" y2="882" stroke="#1a1a1a" stroke-width="1.5" marker-start="url(#arrow-head)" marker-end="url(#arrow-head)"/>
    <text class="dimension-text" x="276" y="610" text-anchor="middle" transform="rotate(-90 276 610)">100mm</text>
  </svg>

  <svg class="front-label" viewBox="0 0 496 624" aria-label="Dunmore Hale Sauvignon Blanc front label">
    <defs>
      <path id="label-outline" d="M248 0 C420 0 496 70 496 215 L496 420 C496 560 400 624 248 624 C96 624 0 560 0 420 L0 215 C0 70 76 0 248 0 Z"/>
      <path id="varietal-arc" d="M58 360 C52 150 140 52 248 52 C356 52 444 150 438 360"/>
      <path id="region-arc" d="M62 440 C82 560 170 592 248 592 C326 592 414 560 434 440"/>
      <radialGradient id="swirl-tone" cx="50%" cy="50%" r="50%">
        <stop offset="0%" stop-color="#f7b844"/>
        <stop offset="70%" stop-color="#f4a526"/>
        <stop offset="100%" stop-color="#d9811a"/>
      </radialGradient>
    </defs>

    <use href="#label-outline" fill="#2c2a26"/>
    <use href="#label-outline" fill="none" stroke="#c9c9c9" stroke-width="6" transform="translate(248 312) scale(0.94) translate(-248 -312)"/>

    <text class="arc-varietal"><textPath href="#varietal-arc" startOffset="50%" text-anchor="middle">SAUVIGNON BLANC</textPath></text>
    <text class="arc-region"><textPath href="#region-arc" startOffset="50%" text-anchor="middle">MARLBOROUGH</textPath></text>

    <rect x="98" y="118" width="300" height="400" rx="72" fill="none" stroke="#c9c9c9" stroke-width="7"/>
    <rect x="110" y="130" width="276" height="376" rx="62" fill="none" stroke="#c9c9c9" stroke-width="2"/>

    <g role="img" aria-label="Side flourish ornament">
      <path d="M52 270 C36 310 36 360 58 405 C46 360 46 310 62 270 Z" fill="#f4a526"/>
    </g>
    <g role="img" aria-label="Side flourish ornament">
      <path d="M444 270 C460 310 460 360 438 405 C450 360 450 310 434 270 Z" fill="#f4a526"/>
    </g>

    <text class="brand-name" x="248" y="190" text-anchor="middle" font-size="54" textLength="236" lengthAdjust="spacingAndGlyphs">DUNMORE</text>
    <text class="brand-name" x="248" y="272" text-anchor="middle" font-size="86" textLength="200" lengthAdjust="spacingAndGlyphs">HALE</text>
    <text class="country" x="248" y="302" text-anchor="middle">NEW ZEALAND</text>

    <ellipse role="img" aria-label="Golden swirl illustration" cx="248" cy="408" rx="102" ry="92" fill="url(#swirl-tone)"/>
  </svg>

</main>
</body>
</html>
```